Jewelry Shop Needs a Business Card Design

***We want a very sharp and unforgettable pantone for the Business Card. ***
***We do not want the business card or logo only in black, white and grey color!!!Please provide us a main color as our brand topic! Thanks!! ***

Mabel’s Nook is a Hong Kong based fine jewelry brand.

We want a very nice, simple and elegant business card design for Mabel's Nook Brand. The company's logo has been uploaded already.

You can design with below info:

Dorian Fung
Director
M: +852 94273658
T: +852 35820417
F: +852 35820419
E: dorian.fung@mabelsnook.example
5/F , Harbourlight Tower, 12-18 Orchid Lane, Wan Tung Kok, Kowloon, Hong Kong

Target Market(s)

Mabel’s Nook philosophy is a jewelry icon of young, creative, trendy, fashionable, stylish, energetic, and elegant. For Mabel’s Nook, jewelry is one collection of artworks, the most important items in personal life.

Industry/Entity Type

Jewelry

Requirements
Must have
• We want a very sharp and unforgettable pantone for the Business Card.

```html
<!DOCTYPE html>
<html lang="en">
<head>
<meta charset="utf-8">
<title>Mabel's Nook — Business Card</title>
<link rel="stylesheet" href="https://fonts.googleapis.com/css2?family=Cormorant+Garamond:ital,wght@0,400;0,500;1,400;1,500&display=swap">
<style>
  :root {
    --page: #ffffff;
    --plum: #5b1a52;
    --plum-deep: #3f0f39;
    --plum-soft: #6a2761;
    --silver: #9c9aa0;
    --ink-light: #f3e9f1;
    --ink-faint: rgba(255, 255, 255, 0.12);
  }
  * { margin: 0; padding: 0; box-sizing: border-box; }
  html, body {
    width: 849px;
    height: 1200px;
    overflow: hidden;
    background: var(--page);
  }
  body {
    position: relative;
    font-family: "Cormorant Garamond", "Times New Roman", serif;
    color: var(--ink-light);
  }
  .card {
    position: absolute;
    left: 252px;
    width: 360px;
    height: 207px;
    background: radial-gradient(ellipse at 50% 40%, var(--plum-soft), var(--plum) 70%);
    overflow: hidden;
  }
  .card--front { top: 274px; }
  .card--back { top: 685px; }

  /* front */
  .brand {
    position: absolute;
    left: 18px;
    top: 8px;
    width: 70px;
    text-align: center;
  }
  .brand__dot {
    display: block;
    width: 40px;
    height: 40px;
    margin: 0 auto 6px;
    border-radius: 50%;
    background: var(--silver);
  }
  .brand__name {
    font-size: 7px;
    letter-spacing: 0.8px;
    text-transform: uppercase;
    color: var(--silver);
    white-space: nowrap;
  }
  .contact {
    position: absolute;
    left: 262px;
    top: 6px;
    list-style: none;
    font-style: italic;
    font-size: 8.5px;
    line-height: 20px;
  }
  .person {
    position: absolute;
    left: 0;
    right: 0;
    top: 82px;
    text-align: center;
    font-style: italic;
  }
  .person__name { font-size: 22px; font-weight: 500; line-height: 24px; }
  .person__role { font-size: 11px; line-height: 14px; }
  .rule {
    position: absolute;
    left: 0;
    right: 0;
    top: 164px;
    height: 7px;
    background: var(--silver);
  }
  .email-strip {
    position: absolute;
    left: 0;
    right: 0;
    top: 178px;
    height: 22px;
    background: var(--plum-deep);
    text-align: center;
    font-style: italic;
    font-size: 10px;
    line-height: 22px;
  }

  /* back */
  .backdrop {
    position: absolute;
    inset: 0;
    background: radial-gradient(circle at 50% 20%, rgba(255,255,255,0.06), transparent 45%);
  }
  .back-mark {
    position: absolute;
    left: 0;
    right: 0;
    top: 64px;
    text-align: center;
    font-size: 22px;
    letter-spacing: 6px;
    text-transform: uppercase;
    color: var(--ink-faint);
  }
  .address {
    position: absolute;
    left: 0;
    right: 0;
    top: 155px;
    text-align: center;
    font-style: italic;
    font-size: 10.5px;
    line-height: 18px;
  }
</style>
</head>
<body>
  <section class="card card--front">
    <div class="brand">
      <span class="brand__dot"></span>
      <p class="brand__name">Mabel’s Nook</p>
    </div>
    <ul class="contact">
      <li>M : +852 94273658</li>
      <li>T : +852 35820417</li>
      <li>F : +852 35820419</li>
    </ul>
    <div class="person">
      <p class="person__name">Dorian Fung</p>
      <p class="person__role">Director</p>
    </div>
    <div class="rule"></div>
    <p class="email-strip">dorian.fung@mabelsnook.example</p>
  </section>

  <section class="card card--back">
    <div class="backdrop" role="img" aria-label="Faint tonal pattern in plum"></div>
    <p class="back-mark">Mabel’s Nook</p>
    <address class="address">
      5/F , Harbourlight Tower, 12-18 Orchid Lane,<br>
      Wan Tung Kok, Kowloon, Hong Kong
    </address>
  </section>
</body>
</html>
```